Website design for Brelvo Quad

Full Website Content Draft for: 'Brelvo Quad - A Financial Freedom Movement'

Header / Navigation
Logo (top left)
Navigation Links: Home | Our Story | Current State | Future State | How You Can Help | The Movement | Get Involved
CTA Button: Join the Movement
Homepage (Hero Section)

Headline:
Empowering Students. Transforming Futures.
Sub-Headline:
Financial literacy isn’t optional anymore — it’s essential.
Body (short):
Every year, millions of college students step into adulthood without the skills to manage money wisely. It’s time to change that.
Call-to-Action Button:
[Join the Movement]
Visual Suggestion:
Full-width image/video of diverse students on campus — upbeat, collaborative, inspiring.
Our Story

Section Header: Our Story
Body Copy:
For too long, financial literacy has been the missing piece of higher education. While students prepare academically for their futures, many graduate with financial stress, poor money habits, and debt that follows them for decades.
We believe knowledge is power — and financial literacy is freedom. With decades of combined experience in banking, leadership, and higher education, our team has seen the struggles firsthand. That’s why we’re committed to starting a movement that ensures every student leaves college not only with a degree, but with financial confidence.
The Current State

Section Header: The Current State
Infographic Copy / Stats:
70% of college students report finances as their #1 source of stress.*
43% of students don’t know their credit score.**
Student loan debt has surpassed $1.7 trillion.***
Subtext:
This is today’s reality. Students deserve better.
Footnotes (to place at bottom of page):
* Norwell Scholastic Wellness Guild, Kestrin Student Vitality Survey, Spring 2022 Report.
** DALMOR & Pexton Pension Partners, Coins Count at School Review (2019).
*** Quillan Monetary Trust of Harbridge, Consumer Credit Data (2024).
Visual Suggestion:
Infographic row with 3 icons (stress, credit, debt) and corresponding stats.
The Future State (Vision)

Section Header: The Future State (Vision)
Body Copy:
Imagine a campus where students graduate with more than a degree — they graduate with financial confidence.
They know how to budget, save, manage credit, and plan for their futures. They are free from fear, better equipped for life after graduation, and ready to thrive personally and professionally.
This is the future we are building together.
Visual Suggestion:
Smiling students celebrating graduation, overlay text “Confidence. Knowledge. Freedom.”
How You Can Help

Section Header: How You Can Help
Copy with Columns:
Universities
Partner with us to bring scalable, student-centered financial education to your campus.
Banks & Financial Institutions
Join us in shaping the next generation of financially confident customers while strengthening community impact.
Students & Parents
Be part of a movement that makes the college experience stronger, not harder.
Call-to-Action Button:
[Contact Us to Partner]
Visual Suggestion:
Three-column layout with icons (graduation cap for Universities, bank building for Banks, heart/people for Students & Parents).
The Movement

Section Header: The Movement
Body Copy:
This isn’t about one campus — it’s about a shift. A national movement to change the financial future for an entire generation. Together, we can rewrite the story.
We believe when students understand money, they reduce stress, gain freedom, and unlock their potential. That’s why this is more than a program — it’s a movement.
Visual Suggestion:
Map of the U.S. with “movement dots” spreading out, or collage of diverse students with bold words: Financial Literacy. Confidence. Future.
Get Involved (Contact Section)

Section Header: Get Involved
Body Copy:
Are you a university leader, bank executive, student, or parent who wants to be part of this movement? Let’s talk.
Contact Form Fields:
Name
Email
Role (University Faculty/Staff, Bank Partner, Student, Parent, Other)
Message
CTA Button: [Submit Interest]
Footer

Copy:
Join us in building the future of financial literacy.
Links: Privacy | Contact | Social Media (Workloom, Snapvale, etc.)

Target Market(s)

Partners: University Faculty and Bank Executives

Industry/Entity Type

Finance and Education

Coding

Number of Pages Required

4 page

Font styles to use
Sans Serif

Colors

Designer to choose colors to be used in the design.

Requirements
Nice to have
• See description for details - This is a website to create a "movement" to help college and university students increase their financial literacy and reduce financial stress,

```html
<!DOCTYPE html>
<html lang="en">
<head>
<meta charset="utf-8">
<title>Brelvo Quad — Website Pages</title>
<link href="https://fonts.googleapis.com/css2?family=Plus+Jakarta+Sans:wght@400;500;600;700;800&display=swap" rel="stylesheet">
<style>
:root{
  --blue:#1a8fd8;
  --blue-dark:#1277b8;
  --ink:#161c2b;
  --muted:#5b6270;
  --line:#e6e9ee;
  --soft:#f5f7fa;
  --footer:#141b2d;
  --footer-text:#aab2c2;
  --stat:#e8421c;
  --backdrop:#9b9b9b;
  --white:#ffffff;
}
*{box-sizing:border-box;margin:0;padding:0}
html,body{width:1200px;height:574px;overflow:hidden;background:var(--backdrop)}
body{font-family:"Plus Jakarta Sans",Arial,sans-serif;color:var(--ink)}
.stage{position:absolute;left:0;top:0;width:2576px;height:1232px;transform:scale(0.46584);transform-origin:0 0}
.page{position:absolute;background:var(--white);overflow:hidden}
.a{position:absolute}
.center{left:0;right:0;text-align:center}
.nav{left:0;right:0;top:0;height:26px;background:var(--white)}
.brand{font-weight:700;font-size:9px;display:flex;align-items:center;gap:3px;color:var(--ink)}
.brand .dot{width:7px;height:7px;background:var(--ink);border-radius:50%}
.brand.light{color:var(--white)}
.brand.light .dot{background:var(--white)}
.links{display:flex;gap:12px;font-size:4.6px;color:var(--ink)}
.links .on{color:var(--blue)}
.btn{background:var(--blue);color:var(--white);font-size:4.6px;font-weight:600;border-radius:3px;display:flex;align-items:center;justify-content:center}
.btn.ghost{background:transparent;border:1px solid var(--blue);color:var(--blue)}
.btn.white{background:var(--white);color:var(--blue)}
.btn.outline-w{background:transparent;border:1px solid var(--white);color:var(--white)}
.h{font-weight:600;color:var(--ink)}
.p{font-size:4.6px;line-height:1.65;color:var(--muted)}
.card{background:var(--white);border:1px solid var(--line);border-radius:3px;box-shadow:0 1px 3px rgba(20,30,50,.06);text-align:center}
.card .t{font-size:5.4px;font-weight:600;margin-top:4px}
.card .d{font-size:4px;color:var(--muted);line-height:1.5;margin-top:3px;padding:0 8px}
.ico{display:block;margin:0 auto}
.foot{left:0;right:0;background:var(--footer);color:var(--footer-text);font-size:4.4px}
.foot .col-h{color:var(--white);font-weight:600;font-size:4.8px;margin-bottom:6px}
.foot .col div{margin-bottom:5px}
.foot .copy{left:0;right:0;text-align:center;font-size:4.2px}
.foot .rule{height:1px;background:#27304a}
.media{border-radius:3px}
.stat-v{font-size:11px;font-weight:700;color:var(--stat)}
.input{border:1px solid #d9dde4;border-radius:2px;font-size:4.4px;color:#8a909c;padding:4px 4px;background:var(--white)}
.lbl{font-size:4.4px;font-weight:600}
</style>
</head>
<body>
<div class="stage">

<!-- HOME PAGE -->
<section class="page" style="left:35px;top:56px;width:573px;height:1120px">
  <div class="a nav">
    <div class="a brand" style="left:44px;top:8px"><span class="dot"></span>Brelvo Quad</div>
    <div class="a links" style="left:240px;top:11px"><span class="on">Home</span><span>About</span><span>Resources</span><span>Contact</span></div>
    <div class="a btn" style="left:491px;top:7px;width:40px;height:13px">Get Started</div>
  </div>
  <div class="a" role="img" aria-label="Students sitting together on a campus lawn with laptops and notebooks" style="left:0;top:26px;width:573px;height:284px;background:linear-gradient(120deg,#3a4a44,#1f2a2c 50%,#3c4136)"></div>
  <div class="a center h" style="top:108px;font-size:19px;line-height:1.05;color:var(--white);font-weight:700">Unlock Your Financial<br>Potential</div>
  <div class="a center" style="top:157px;font-size:5.6px;line-height:1.6;color:#e8ecf2;padding:0 185px">Join Brelvo Quad, a financial freedom movement empowering students to achieve their financial goals. Learn essential money management skills, access exclusive resources, and connect with a supportive community.</div>
  <div class="a btn" style="left:220px;top:208px;width:73px;height:19px">Get Started Today</div>
  <div class="a btn outline-w" style="left:298px;top:208px;width:55px;height:19px">Learn More</div>

  <div class="a center h" style="top:337px;font-size:11px">The Current State</div>
  <div class="a center p" style="top:355px;padding:0 170px">Students face significant financial challenges that impact their well-being and future success.</div>
  <div class="a card" style="left:42px;top:395px;width:156px;height:39px;padding-top:8px"><div class="stat-v">70%</div><div class="d" style="margin-top:2px">of students report finances as their #1 source of stress</div></div>
  <div class="a card" style="left:209px;top:395px;width:155px;height:39px;padding-top:8px"><div class="stat-v">43%</div><div class="d" style="margin-top:2px">don't know their credit score</div></div>
  <div class="a card" style="left:375px;top:395px;width:156px;height:39px;padding-top:8px"><div class="stat-v">$1.7T</div><div class="d" style="margin-top:2px">total student loan debt nationwide</div></div>

  <div class="a center h" style="top:487px;font-size:15px">Get Involved</div>
  <div class="a center p" style="top:508px;padding:0 170px">Join the movement to empower students with financial literacy and freedom. Whether you're a university, bank, or student, there's a way for you to contribute.</div>
  <div class="a center h" style="top:543px;font-size:9px">How You Can Help</div>
  <div class="a card" style="left:42px;top:566px;width:156px;height:65px;padding-top:10px">
    <svg class="ico" width="12" height="12" viewBox="0 0 12 12"><circle cx="6" cy="6" r="6" fill="#e3f1fb"/><path d="M3 5l3-1.5L9 5 6 6.5z" fill="none" stroke="var(--blue)" stroke-width=".7"/></svg>
    <div class="t">Universities</div><div class="d">Bring Brelvo Quad into your curriculum and offer our resources to your students.</div></div>
  <div class="a card" style="left:209px;top:566px;width:155px;height:65px;padding-top:10px">
    <svg class="ico" width="12" height="12" viewBox="0 0 12 12"><circle cx="6" cy="6" r="6" fill="#e3f1fb"/><path d="M3.5 8.5h5M4 5v3M6 5v3M8 5v3M3.5 4.5L6 3l2.5 1.5z" fill="none" stroke="var(--blue)" stroke-width=".6"/></svg>
    <div class="t">Banks</div><div class="d">Partner with us to provide financial education and tools to students.</div></div>
  <div class="a card" style="left:375px;top:566px;width:156px;height:65px;padding-top:10px">
    <svg class="ico" width="12" height="12" viewBox="0 0 12 12"><circle cx="6" cy="6" r="6" fill="#e3f1fb"/><circle cx="6" cy="6" r="2.4" fill="none" stroke="var(--blue)" stroke-width=".7"/><circle cx="6" cy="6" r="1" fill="var(--blue)"/></svg>
    <div class="t">Students &amp; Parents</div><div class="d">Access our free resources and workshops to improve your financial literacy.</div></div>

  <div class="a center h" style="top:652px;font-size:9.5px">Hear from the Brelvo Community</div>
  <div class="a card" style="left:42px;top:675px;width:239px;height:160px;text-align:left">
    <div role="img" aria-label="Video still of a student speaking in a school hallway" style="height:129px;background:linear-gradient(135deg,#6b4a32,#2e2a2a 60%,#4d3a2c)"></div>
    <div style="font-size:5px;font-weight:600;margin:8px 0 0 8px">Building Financial Freedom</div>
    <div style="font-size:3.8px;color:var(--muted);margin:1px 0 0 8px">A student's journey to financial literacy</div>
  </div>
  <div class="a" style="left:154px;top:735px;width:16px;height:16px;border-radius:50%;background:var(--white);opacity:.9"></div>
  <svg class="a" style="left:159px;top:739px" width="8" height="8" viewBox="0 0 8 8"><path d="M1 0l6 4-6 4z" fill="var(--blue)"/></svg>
  <div class="a card" style="left:292px;top:675px;width:239px;height:160px;text-align:left">
    <div role="img" aria-label="Video still of a student speaking in a bright campus lounge" style="height:129px;background:linear-gradient(135deg,#6f7a6a,#4c4a44 55%,#8a8468)"></div>
    <div style="font-size:5px;font-weight:600;margin:8px 0 0 8px">Investing in the Future</div>
    <div style="font-size:3.8px;color:var(--muted);margin:1px 0 0 8px">How Brelvo empowers universities</div>
  </div>
  <div class="a" style="left:403px;top:732px;width:16px;height:16px;border-radius:50%;background:var(--white);opacity:.9"></div>
  <svg class="a" style="left:408px;top:736px" width="8" height="8" viewBox="0 0 8 8"><path d="M1 0l6 4-6 4z" fill="var(--blue)"/></svg>

  <div class="a" style="left:0;top:883px;width:573px;height:122px;background:var(--blue)"></div>
  <div class="a center" style="top:910px;font-size:11.5px;font-weight:600;color:var(--white)">Ready to Transform Student Finances?</div>
  <div class="a center" style="top:928px;font-size:5.4px;line-height:1.6;color:#dbeefa;padding:0 175px">Join the movement that's changing how students approach financial literacy nationwide.</div>
  <div class="a btn white" style="left:208px;top:958px;width:75px;height:20px">Start Your Journey</div>
  <div class="a btn outline-w" style="left:289px;top:958px;width:75px;height:20px">Explore Resources</div>

  <div class="a foot" style="top:1005px;height:115px">
    <div class="a brand light" style="left:44px;top:18px"><span class="dot"></span>Brelvo Quad</div>
    <div class="a" style="left:42px;top:36px;width:245px;line-height:1.6">Empowering students to achieve financial freedom through education, resources, and community support.</div>
    <div class="a" style="left:42px;top:57px;display:flex;gap:7px"><span>Workloom</span><span>Chirpline</span><span>Snapvale</span></div>
    <div class="a col" style="left:292px;top:18px"><div class="col-h">Navigation</div><div>Home</div><div>About</div><div>Resources</div><div>Contact</div></div>
    <div class="a col" style="left:417px;top:18px"><div class="col-h">Legal</div><div>Privacy Policy</div><div>Terms of Service</div></div>
    <div class="a rule" style="left:42px;right:42px;top:84px"></div>
    <div class="a copy" style="top:92px">© 2024 Brelvo Quad. All rights reserved.</div>
  </div>
</section>

<!-- ABOUT PAGE -->
<section class="page" style="left:630px;top:56px;width:583px;height:1120px;background:var(--soft)">
  <div class="a nav" style="background:var(--soft)">
    <div class="a brand" style="left:44px;top:8px"><span class="dot"></span>Brelvo Quad</div>
    <div class="a links" style="left:236px;top:11px"><span>Home</span><span class="on">About</span><span>Resources</span><span>Contact</span></div>
    <div class="a btn" style="left:483px;top:7px;width:57px;height:13px">Join the Movement</div>
  </div>
  <div class="a center" style="top:72px;font-size:5px;font-weight:600;color:var(--blue)">Our Mission</div>
  <div class="a center h" style="top:85px;font-size:16px;line-height:1.05;font-weight:700">A Financial Freedom Movement for<br>Students</div>
  <div class="a center p" style="top:126px">Learn about our origins and the vision that drives us to empower the next generation of leaders.</div>

  <div class="a h" style="left:43px;top:196px;font-size:9px">Our Story</div>
  <div class="a p" style="left:43px;top:213px;width:238px;font-size:4.3px;line-height:1.6">Brelvo Quad began with a simple idea: to empower students across the nation with the knowledge and tools to achieve financial freedom. Founded by a group of passionate educators and financial experts, we recognized the critical need for accessible financial education tailored to the unique challenges and opportunities faced by students. Our journey started with pilot programs at a few universities, quickly gaining momentum as students experienced tangible improvements in their financial well-being. Today, Brelvo Quad is a thriving community, dedicated to transforming the financial landscape for students nationwide.</div>
  <div class="a h" style="left:43px;top:281px;font-size:9px">The Movement</div>
  <div class="a p" style="left:43px;top:297px;width:238px;font-size:4.3px;line-height:1.6">Brelvo Quad is more than just a program; it's a national movement. Our vision is to create a ripple effect of financial empowerment, starting with students and extending to their families and communities. We envision a future where every student has the confidence and capability to navigate their financial journey successfully, free from the burdens of debt and equipped to build a prosperous future. Join us as we work to make financial freedom a reality for all students.</div>
  <div class="a media" role="img" aria-label="Dark map of the United States with glowing dots linking campuses across the country" style="left:302px;top:178px;width:238px;height:178px;background:radial-gradient(circle at 50% 45%,#3c5878,#1b2c47 70%);box-shadow:0 4px 10px rgba(20,30,50,.25)"></div>

  <div class="a" style="left:0;top:400px;width:583px;height:170px;background:var(--white);opacity:.5"></div>
  <div class="a center h" style="top:426px;font-size:11px">Our Core Values</div>
  <div class="a center p" style="top:446px">These principles guide everything we do at Brelvo Quad.</div>
  <div class="a card" style="left:43px;top:477px;width:158px;height:65px;padding-top:8px">
    <svg class="ico" width="10" height="10" viewBox="0 0 10 10"><circle cx="5" cy="4" r="2.8" fill="none" stroke="var(--blue)" stroke-width=".8"/><path d="M4 7.5h2M4.2 9h1.6" stroke="var(--blue)" stroke-width=".8"/></svg>
    <div class="t">Knowledge</div><div class="d">Students understand budgeting, saving, and financial planning</div></div>
  <div class="a card" style="left:212px;top:477px;width:158px;height:65px;padding-top:8px">
    <div style="height:10px"></div>
    <div class="t">Confidence</div><div class="d">Graduates feel prepared for financial challenges ahead</div></div>
  <div class="a card" style="left:381px;top:477px;width:158px;height:65px;padding-top:8px">
    <svg class="ico" width="10" height="10" viewBox="0 0 10 10"><path d="M2 8l2-4 4-3-1 4-4 2z" fill="var(--blue)"/></svg>
    <div class="t">Freedom</div><div class="d">Financial stress is replaced with opportunity and growth</div></div>

  <div class="a center h" style="top:597px;font-size:11px">Meet Our Team</div>
  <div class="a center p" style="top:616px">Passionate leaders driving the financial literacy movement forward.</div>
  <div class="a" style="left:101px;top:646px;width:43px;height:43px;border-radius:50%;background:var(--blue);color:var(--white);font-size:11px;font-weight:600;display:flex;align-items:center;justify-content:center">OT</div>
  <div class="a" style="left:270px;top:646px;width:43px;height:43px;border-radius:50%;background:var(--blue);color:var(--white);font-size:11px;font-weight:600;display:flex;align-items:center;justify-content:center">LM</div>
  <div class="a" style="left:439px;top:646px;width:43px;height:43px;border-radius:50%;background:var(--blue);color:var(--white);font-size:11px;font-weight:600;display:flex;align-items:center;justify-content:center">TB</div>
  <div class="a" style="left:43px;top:697px;width:158px;text-align:center"><div style="font-size:5.4px;font-weight:600">Owen Tarrell</div><div style="font-size:4.2px;color:var(--blue);font-weight:600;margin-top:4px">Founder &amp; CEO</div><div class="p" style="font-size:3.9px;line-height:1.5;margin-top:3px">Former banking executive with 15+ years in financial education and student advocacy.</div></div>
  <div class="a" style="left:212px;top:697px;width:158px;text-align:center"><div style="font-size:5.4px;font-weight:600">Lena Marsh</div><div style="font-size:4.2px;color:var(--blue);font-weight:600;margin-top:4px">Head of University Relations</div><div class="p" style="font-size:3.9px;line-height:1.5;margin-top:3px">Higher education specialist focused on student success and financial wellness programs.</div></div>
  <div class="a" style="left:381px;top:697px;width:158px;text-align:center"><div style="font-size:5.4px;font-weight:600">Theo Brandt</div><div style="font-size:4.2px;color:var(--blue);font-weight:600;margin-top:4px">Director of Partnerships</div><div class="p" style="font-size:3.9px;line-height:1.5;margin-top:3px">Banking industry veteran building strategic partnerships with financial institutions.</div></div>

  <div class="a" style="left:0;top:758px;width:583px;height:122px;background:var(--blue)"></div>
  <div class="a center" style="top:784px;font-size:11px;font-weight:600;color:var(--white)">Our Impact</div>
  <div class="a center" style="top:805px;font-size:5px;color:#dbeefa">The numbers speak for themselves - we're making a real difference.</div>
  <div class="a" style="left:43px;top:829px;width:497px;display:flex;justify-content:space-between;color:var(--white);text-align:center">
    <div style="width:120px"><div style="font-size:11px;font-weight:600">50+</div><div style="font-size:4.2px;color:#dbeefa;margin-top:4px">Partner Universities</div></div>
    <div style="width:120px"><div style="font-size:11px;font-weight:600">100K+</div><div style="font-size:4.2px;color:#dbeefa;margin-top:4px">Students Reached</div></div>
    <div style="width:120px"><div style="font-size:11px;font-weight:600">25+</div><div style="font-size:4.2px;color:#dbeefa;margin-top:4px">Bank Partners</div></div>
    <div style="width:120px"><div style="font-size:11px;font-weight:600">85%</div><div style="font-size:4.2px;color:#dbeefa;margin-top:4px">Report Improved Confidence</div></div>
  </div>

  <div class="a" style="left:0;top:880px;width:583px;height:125px;background:var(--white)"></div>
  <div class="a center h" style="top:908px;font-size:11px">Ready to Join Our Mission?</div>
  <div class="a center p" style="top:927px;padding:0 180px">Be part of the movement that's transforming how students approach financial literacy.</div>
  <div class="a btn" style="left:213px;top:956px;width:75px;height:21px">Get Started Today</div>
  <div class="a btn ghost" style="left:293px;top:956px;width:77px;height:21px">Explore Resources</div>

  <div class="a foot" style="top:1005px;height:115px">
    <div class="a brand light" style="left:44px;top:18px"><span class="dot"></span>Brelvo Quad</div>
    <div class="a" style="left:43px;top:36px;width:115px;line-height:1.6;font-size:4px">Empowering students to achieve financial freedom.</div>
    <div class="a col" style="left:170px;top:18px;font-size:4px"><div class="col-h">Navigation</div><div>Home</div><div>About</div><div>Resources</div><div>Community</div></div>
    <div class="a col" style="left:297px;top:18px;font-size:4px"><div class="col-h">Legal</div><div>Privacy Policy</div><div>Terms of Service</div></div>
    <div class="a col" style="left:423px;top:18px;font-size:4px"><div class="col-h">Connect</div><div>Contact Us</div><div>Workloom</div><div>Chirpline</div></div>
    <div class="a rule" style="left:43px;right:43px;top:84px"></div>
    <div class="a copy" style="top:93px;font-size:4px">© 2024 Brelvo Quad. All rights reserved.</div>
  </div>
</section>

<!-- RESOURCES PAGE -->
<section class="page" style="left:1233px;top:56px;width:643px;height:1120px">
  <div class="a nav">
    <div class="a brand" style="left:49px;top:9px"><span class="dot"></span>Brelvo Quad</div>
    <div class="a links" style="left:270px;top:13px"><span>Home</span><span>About</span><span class="on">Resources</span><span>Contact</span></div>
    <div class="a btn" style="left:551px;top:8px;width:45px;height:14px">Get Started</div>
  </div>
  <div class="a media" role="img" aria-label="Illustration of students walking together with books and laptops under floating finance icons" style="left:137px;top:54px;width:369px;height:178px;background:linear-gradient(180deg,#6aa6e6,#4d8fdc)"></div>
  <div class="a center h" style="top:274px;font-size:22px;line-height:1.02;font-weight:700">Empowering Students Towards<br>Financial Freedom</div>
  <div class="a center p" style="top:327px;padding:0 193px;font-size:5.4px">Brelvo Quad is a movement dedicated to equipping students with the knowledge and tools to navigate their financial journey successfully. We believe in a future where every student can achieve financial independence and thrive.</div>
  <div class="a btn" style="left:297px;top:369px;width:50px;height:16px">Learn More</div>

  <div class="a h" style="left:137px;top:428px;font-size:10px">The Current State</div>
  <div class="a p" style="left:137px;top:446px;width:369px;font-size:4.6px">Many students face significant financial challenges during their academic careers. These challenges can impact their well-being, academic performance, and future prospects. Here's a snapshot of the current landscape:</div>
  <div class="a card" style="left:137px;top:480px;width:116px;height:48px;padding-top:11px">
    <svg class="ico" width="9" height="9" viewBox="0 0 9 9"><circle cx="4.5" cy="4.5" r="3.8" fill="none" stroke="var(--blue)" stroke-width=".7"/><path d="M3 5.5q1.5 1 3 0" fill="none" stroke="var(--blue)" stroke-width=".6"/></svg>
    <div class="t">High Stress Levels</div></div>
  <div class="a card" style="left:263px;top:480px;width:116px;height:48px;padding-top:11px">
    <svg class="ico" width="9" height="9" viewBox="0 0 9 9"><rect x=".8" y="2" width="7.4" height="5" rx=".6" fill="none" stroke="var(--blue)" stroke-width=".7"/><path d="M.8 3.6h7.4" stroke="var(--blue)" stroke-width=".7"/></svg>
    <div class="t">Credit Dependence</div></div>
  <div class="a card" style="left:389px;top:480px;width:116px;height:48px;padding-top:11px">
    <svg class="ico" width="9" height="9" viewBox="0 0 9 9"><rect x=".8" y="2" width="7.4" height="5" rx=".6" fill="none" stroke="var(--blue)" stroke-width=".7"/><circle cx="4.5" cy="4.5" r="1.2" fill="var(--blue)"/></svg>
    <div class="t">Mounting Debt</div></div>
  <div class="a p" style="left:137px;top:542px;width:369px;font-size:4.4px;line-height:1.7">Studies show that a significant percentage of students experience high levels of financial stress, often leading to anxiety and depression. Many rely heavily on credit cards to cover expenses, accumulating debt with high interest rates. The average student loan debt continues to rise, creating a substantial burden for graduates entering the workforce.</div>

  <div class="a h" style="left:137px;top:592px;font-size:10px">The Future State (Vision)</div>
  <div class="a p" style="left:137px;top:611px;width:369px;font-size:4.6px">At Brelvo Quad, we envision a future where students are financially confident and prepared for success. Our vision includes:</div>
  <div class="a card" style="left:137px;top:645px;width:116px;height:48px;padding-top:11px">
    <svg class="ico" width="9" height="9" viewBox="0 0 9 9"><path d="M.8 3.5L4.5 2l3.7 1.5L4.5 5z M2.5 4.3v2l2 .9 2-.9v-2" fill="none" stroke="var(--blue)" stroke-width=".6"/></svg>
    <div class="t">Financial Literacy</div></div>
  <div class="a card" style="left:263px;top:645px;width:116px;height:48px;padding-top:11px">
    <svg class="ico" width="9" height="9" viewBox="0 0 9 9"><path d="M.8 6.5l2.5-2.5 1.8 1.5 3-3M6 2.5h2.1v2" fill="none" stroke="var(--blue)" stroke-width=".7"/></svg>
    <div class="t">Smart Financial Habits</div></div>
  <div class="a card" style="left:389px;top:645px;width:116px;height:48px;padding-top:11px">
    <svg class="ico" width="9" height="9" viewBox="0 0 9 9"><circle cx="4.5" cy="3.5" r="2.5" fill="none" stroke="var(--blue)" stroke-width=".7"/><path d="M3.3 5.7l-.6 2.6 1.8-.9 1.8.9-.6-2.6" fill="none" stroke="var(--blue)" stroke-width=".6"/></svg>
    <div class="t">Debt-Free Graduation</div></div>
  <div class="a p" style="left:137px;top:706px;width:369px;font-size:4.4px;line-height:1.7">We aim to empower students with the knowledge and skills to manage their finances effectively, make informed decisions, and build healthy financial habits. Our goal is to see more students graduate with minimal or no debt, ready to pursue their dreams without the weight of financial burdens.</div>

  <div class="a media" role="img" aria-label="Graduates in caps and gowns celebrating outside a campus building" style="left:137px;top:757px;width:369px;height:123px;background:linear-gradient(135deg,#45556b,#1d2636 55%,#3a475a)"></div>

  <div class="a center h" style="top:904px;font-size:11px">Ready to Take Control?</div>
  <div class="a center p" style="top:923px;padding:0 215px;font-size:5.2px">Join a community of students who are building a brighter financial future. It's time to thrive.</div>
  <div class="a btn" style="left:285px;top:950px;width:73px;height:18px">Join the Movement</div>

  <div class="a foot" style="top:992px;height:128px">
    <div class="a brand light" style="left:49px;top:19px"><span class="dot"></span>Brelvo Quad</div>
    <div class="a" style="left:47px;top:39px;width:275px;line-height:1.6">Empowering students to achieve financial freedom through education, resources, and community support.</div>
    <div class="a" style="left:47px;top:62px;display:flex;gap:7px"><span>Workloom</span><span>Chirpline</span><span>Snapvale</span></div>
    <div class="a col" style="left:327px;top:19px"><div class="col-h">Navigation</div><div>Home</div><div>About</div><div>Resources</div><div>Contact</div></div>
    <div class="a col" style="left:467px;top:19px"><div class="col-h">Legal</div><div>Privacy Policy</div><div>Terms of Service</div></div>
    <div class="a rule" style="left:47px;right:47px;top:92px"></div>
    <div class="a copy" style="top:102px">© 2024 Brelvo Quad. All rights reserved.</div>
  </div>
</section>

<!-- CONTACT PAGE -->
<section class="page" style="left:1898px;top:56px;width:643px;height:469px;background:var(--soft)">
  <div class="a nav" style="background:var(--soft)">
    <div class="a brand" style="left:49px;top:9px"><span class="dot"></span>Brelvo Quad</div>
    <div class="a links" style="left:270px;top:13px"><span>Home</span><span>About</span><span>Resources</span><span class="on">Contact</span></div>
    <div class="a btn" style="left:551px;top:8px;width:45px;height:14px">Get Started</div>
  </div>
  <div class="a center h" style="top:52px;font-size:18px;font-weight:700">Contact Us</div>
  <div class="a center p" style="top:78px;padding:0 200px;font-size:5.2px">Ready to join the movement? Get in touch with us and let's work together to empower students with financial literacy.</div>
  <div class="a" style="left:107px;top:117px;width:428px;height:200px;background:var(--white);border-radius:3px;box-shadow:0 2px 6px rgba(20,30,50,.08)"></div>
  <div class="a center h" style="top:129px;font-size:10.5px">Let's Connect</div>
  <div class="a lbl" style="left:214px;top:154px">Name</div>
  <div class="a lbl" style="left:326px;top:154px">Email</div>
  <div class="a input" style="left:214px;top:163px;width:103px;height:16px">Your Name</div>
  <div class="a input" style="left:326px;top:163px;width:102px;height:16px">Your Email</div>
  <div class="a lbl" style="left:214px;top:190px">Role</div>
  <div class="a input" style="left:214px;top:199px;width:214px;height:15px;color:var(--ink)">Select Your Role</div>
  <svg class="a" style="left:419px;top:205px" width="5" height="3" viewBox="0 0 5 3"><path d="M.5.5l2 2 2-2" fill="none" stroke="var(--ink)" stroke-width=".6"/></svg>
  <div class="a lbl" style="left:214px;top:225px">Message</div>
  <div class="a input" style="left:214px;top:234px;width:214px;height:42px">Your Message</div>
  <div class="a btn" style="left:302px;top:288px;width:38px;height:16px">Submit</div>

  <div class="a foot" style="top:341px;height:128px">
    <div class="a brand light" style="left:49px;top:19px"><span class="dot"></span>Brelvo Quad</div>
    <div class="a" style="left:47px;top:39px;width:275px;line-height:1.6">Empowering students to achieve financial freedom through education, resources, and community support.</div>
    <div class="a" style="left:47px;top:62px;display:flex;gap:7px"><span>Workloom</span><span>Chirpline</span><span>Snapvale</span></div>
    <div class="a col" style="left:327px;top:19px"><div class="col-h">Navigation</div><div>Home</div><div>About</div><div>Resources</div><div>Contact</div></div>
    <div class="a col" style="left:467px;top:19px"><div class="col-h">Legal</div><div>Privacy Policy</div><div>Terms of Service</div></div>
    <div class="a rule" style="left:47px;right:47px;top:92px"></div>
    <div class="a copy" style="top:102px">© 2024 Brelvo Quad. All rights reserved.</div>
  </div>
</section>

</div>
</body>
</html>
```